TrueGrindz Complete Stationery - Logo already designed

I already have the logo designed see attached. I need have a full set of stationary and business card designed for printing. I have attached an example of what I mean.

Please feel free to be creative. Also you can use the X in the logo by its self if you think it will work.

My details:

Name: Corwin Lestak
Social media handles: @corwinlestak
W: corwinlestak.com
E: info@corwinlestak.com
​P: 08 7493 5286
PO Box 7382, Marlowe Bay 6027
ABN 83 402 719 265

Target Market(s)

Anyone looking to be inspired.

Industry/Entity Type

Business

Font styles to use
Sans Serif

Colors
fbee3e
000000

Requirements
Must have
• My details:
• Name: Corwin Lestak
• Social media handles: @corwinlestak
• W: corwinlestak.com
• E: info@corwinlestak.com
• ​P: 08 7493 5286
• PO Box 7382, Marlowe Bay 6027
• ABN 83 402 719 265
Nice to have
• Something a little different
Should not have
• must not look tacky.

```html
<!DOCTYPE html>
<html lang="en">
<head>
<meta charset="utf-8">
<title>TrueGrindz Stationery – Corwin Lestak</title>
<link rel="stylesheet" href="https://fonts.googleapis.com/css2?family=Arimo&family=Barlow:wght@500;600;800&display=swap">
<style>
:root{
  --yellow:#fbdc14;
  --black:#111111;
  --charcoal:#3a3a3c;
  --paper:#ffffff;
  --paper-soft:#f3f3f3;
  --body-grey:#6a6f7a;
  --backdrop:#ecebe8;
  --line-grey:#555555;
}
*{box-sizing:border-box;margin:0;padding:0}
html,body{width:1200px;height:801px;overflow:hidden;background:var(--backdrop)}
body{position:relative;font-family:"Barlow",Arial,sans-serif;color:var(--black)}
.sheet{position:absolute;background:var(--paper);box-shadow:0 2px 6px rgba(0,0,0,.18)}
.name{font-family:"Barlow",Arial,sans-serif;font-weight:800;letter-spacing:.5px;text-shadow:1px 2px 2px rgba(0,0,0,.25);line-height:1}
.brand{font-family:"Barlow",Arial,sans-serif;font-weight:800;line-height:1;white-space:nowrap}
.icon{width:9px;height:9px;vertical-align:-1px;margin-right:4px}
.contact{font-weight:500;white-space:nowrap}

/* Letterhead */
.letterhead{left:59px;top:59px;width:528px;height:701px;background:linear-gradient(var(--paper),var(--paper-soft))}
.letterhead__topbar{position:absolute;left:0;top:0;width:100%;height:4px;background:var(--line-grey)}
.letterhead .name{position:absolute;left:23px;top:53px;font-size:31px}
.letterhead .brand{position:absolute;left:295px;top:50px;font-size:30px;color:var(--black)}
.letterhead__rule{position:absolute;left:8px;right:6px;top:110px;height:1.5px;background:var(--line-grey)}
.letterhead__body{position:absolute;left:28px;width:476px;top:149px;font-family:"Arimo",Arial,sans-serif;font-size:12.1px;line-height:15.2px;color:var(--body-grey);text-align:justify}
.letterhead__body p{margin-bottom:15.2px}
.letterhead__closing{position:absolute;right:28px;top:548px;font-family:"Arimo",Arial,sans-serif;font-size:12.5px;color:var(--black)}
.letterhead__signature{position:absolute;right:33px;top:566px;width:72px;height:30px;background:linear-gradient(90deg,#e6e6e6,#f2f2f2);border-radius:4px}
.letterhead__footer{position:absolute;left:0;top:598px;width:100%;height:72px;background:var(--yellow);font-size:12.3px;text-align:center;padding-top:18px;line-height:20px}
.letterhead__footer::after{content:"";position:absolute;left:0;right:0;bottom:9px;height:1.5px;background:var(--black)}
.letterhead__footer .contact{margin:0 5px}

/* Business cards */
.card{width:226px;height:127px;overflow:hidden}
.card--front{left:635px;top:34px}
.card--front .name{position:absolute;left:0;right:0;top:30px;text-align:center;font-size:22px}
.card--front .card__band{position:absolute;left:0;right:0;top:65px;bottom:0;background:var(--charcoal);border-top:2px solid var(--yellow)}
.card--front .brand{position:absolute;left:0;right:0;top:82px;text-align:center;font-size:26px;color:var(--yellow)}
.card--back{left:922px;top:33px;background:linear-gradient(var(--paper),var(--paper-soft))}
.card--back .card__band{position:absolute;left:0;right:0;top:0;height:25px;background:var(--black);border-bottom:2px solid var(--yellow)}
.card--back .brand{position:absolute;left:0;right:0;top:5px;text-align:center;font-size:14px;color:var(--yellow)}
.card__details{position:absolute;left:9px;top:48px;font-size:7.4px;line-height:15px}
.card__details .icon{width:7px;height:7px}
.card__row span+span{margin-left:26px}

/* Envelope front */
.envelope{left:619px;top:195px;width:554px;height:276px}
.envelope .name{position:absolute;left:35px;top:52px;font-size:22px}
.envelope__brandbox{position:absolute;left:0;top:82px;width:217px;height:64px;background:var(--charcoal);box-shadow:1px 1px 2px rgba(0,0,0,.3)}
.envelope__brandbox .brand{position:absolute;left:0;right:0;top:17px;text-align:center;font-size:28px;color:var(--yellow)}
.envelope__window{position:absolute;left:261px;top:55px;width:262px;height:132px;border:1.5px solid var(--black);border-radius:20px}
.envelope__window i{position:absolute;left:24px;right:16px;border-top:1.5px dotted #333}
.envelope__footer{position:absolute;left:0;right:0;top:216px;height:46px;background:var(--yellow);border-top:1.5px solid var(--black);border-bottom:1.5px solid var(--black);font-size:7.4px;line-height:17px}
.envelope__footer .col{position:absolute;top:5px}
.envelope__footer .icon{width:7px;height:7px}

/* Envelope back */
.envelope-back{left:617px;top:502px;width:555px;height:276px}
.envelope-back svg{position:absolute;left:0;top:0}
</style>
</head>
<body>

<section class="sheet letterhead" aria-label="Letterhead">
  <div class="letterhead__topbar"></div>
  <h1 class="name">CORWIN LESTAK</h1>
  <div class="brand">TrueGrindz</div>
  <div class="letterhead__rule"></div>
  <div class="letterhead__body">
    <p>Tempor arcu Varius mattis luctus massa, viverra massa vestibulum curae; aliquam quisque ante molestie urna vitae magna eros class ultrices. Nam sit nec, nisl nonummy urna. Donec hendrerit velit magna vitae amet natoque class quis egestas. Ultricies feugiat adipiscing fermentum fames potenti vitae pharetra parturient et vitae enim iaculis laoreet turpis sociosqu. Lectus. Pretium nostra primis proin bibendum. Amet nisi suscipit curabitur aenean tempor. Quisque hymenaeos dapibus facilisi. Curae; fames facilisi bibendum inceptos auctor bibendum nullam.</p>
    <p>Faucibus ac at Ut consectetuer sem, conubia. Habitant. Dictumst placerat laoreet ullamcorper viverra accumsan, hac. Non mauris erat pulvinar nisi rutrum tortor odiosodales. Euismod inceptos convallis laoreet condimentum erat conubia. Platea class.Suscipit nisi ornare congue.</p>
    <p>Congue. Amet nonummy integer dictum nostra orci Habitasse porta rhoncus leo justo mauris torquent magnis, sociis ornare cursus nec, eu suspendisse risus mollis. Consequat ultrices sit Dolor turpis blandit hendrerit ornare per Eros nisl massa.</p>
    <p>Amet vitae vitae ornare erat dictum per taciti et a hendrerit. Mattis per pellentesque vehicula nulla lacus placerat fusce tempor amet primis praesent facilisi ridiculus luctus elementum conubia lobortis. Convallis. Nulla curabitur conubia. Ullamcorper curae; erat conubia amet auctor rhoncus faucibus. Netus scelerisque. Euismod. amet id pellentesque nam senectus duis magnis quis</p>
  </div>
  <div class="letterhead__closing">your sincerely</div>
  <div class="letterhead__signature" role="img" aria-label="Handwritten signature"></div>
  <footer class="letterhead__footer">
    <div>
      <span class="contact"><svg class="icon" viewBox="0 0 10 10"><rect x="2" y="0.5" width="6" height="9" rx="1.2" fill="none" stroke="#111" stroke-width="1.2"/></svg>08 7493 5286</span>
      <span class="contact"><svg class="icon" viewBox="0 0 10 10"><path d="M5 10 L1.8 5 A3.6 3.6 0 1 1 8.2 5 Z" fill="#111"/><circle cx="5" cy="3.6" r="1.2" fill="#fbdc14"/></svg>PO Box 7382, Marlowe Bay 6027 &nbsp; ABN 83 402 719 265</span>
    </div>
    <div>
      <span class="contact"><svg class="icon" viewBox="0 0 10 10"><circle cx="5" cy="5" r="4.2" fill="none" stroke="#111"/><path d="M1 5H9M5 1V9" stroke="#111" stroke-width=".8"/></svg>corwinlestak.com</span>
      <span class="contact"><svg class="icon" viewBox="0 0 10 10"><rect x="0.7" y="2" width="8.6" height="6" fill="none" stroke="#111"/><path d="M1 2.3L5 5.5L9 2.3" fill="none" stroke="#111"/></svg>info@corwinlestak.com</span>
      <span class="contact">Social media handles: @corwinlestak</span>
    </div>
  </footer>
</section>

<section class="sheet card card--front" aria-label="Business card front">
  <h2 class="name">CORWIN LESTAK</h2>
  <div class="card__band"></div>
  <div class="brand">TrueGrindz</div>
</section>

<section class="sheet card card--back" aria-label="Business card back">
  <div class="card__band"></div>
  <div class="brand">TrueGrindz</div>
  <div class="card__details">
    <div class="card__row"><span class="contact"><svg class="icon" viewBox="0 0 10 10"><rect x="2" y="0.5" width="6" height="9" rx="1.2" fill="none" stroke="#111" stroke-width="1.2"/></svg>08 7493 5286</span></div>
    <div class="card__row"><span class="contact"><svg class="icon" viewBox="0 0 10 10"><path d="M5 10 L1.8 5 A3.6 3.6 0 1 1 8.2 5 Z" fill="#111"/></svg>PO Box 7382, Marlowe Bay 6027 &nbsp; ABN 83 402 719 265</span></div>
    <div class="card__row"><span class="contact"><svg class="icon" viewBox="0 0 10 10"><circle cx="5" cy="5" r="4.2" fill="none" stroke="#111"/></svg>corwinlestak.com</span><span class="contact"><svg class="icon" viewBox="0 0 10 10"><rect x="0.7" y="2" width="8.6" height="6" fill="none" stroke="#111"/></svg>info@corwinlestak.com</span></div>
    <div class="card__row"><span class="contact">Social media handles: @corwinlestak</span></div>
  </div>
</section>

<section class="sheet envelope" aria-label="Envelope front">
  <h2 class="name">CORWIN LESTAK</h2>
  <div class="envelope__brandbox"><div class="brand">TrueGrindz</div></div>
  <div class="envelope__window"><i style="top:38px"></i><i style="top:67px"></i><i style="top:97px"></i></div>
  <footer class="envelope__footer">
    <div class="col" style="left:27px">
      <div class="contact"><svg class="icon" viewBox="0 0 10 10"><rect x="2" y="0.5" width="6" height="9" rx="1.2" fill="none" stroke="#111" stroke-width="1.2"/></svg>08 7493 5286</div>
      <div class="contact"><svg class="icon" viewBox="0 0 10 10"><path d="M5 10 L1.8 5 A3.6 3.6 0 1 1 8.2 5 Z" fill="#111"/></svg>PO Box 7382, Marlowe Bay 6027 &nbsp; ABN 83 402 719 265</div>
    </div>
    <div class="col" style="left:257px;top:13px">
      <div><span class="contact"><svg class="icon" viewBox="0 0 10 10"><circle cx="5" cy="5" r="4.2" fill="none" stroke="#111"/></svg>corwinlestak.com</span> &nbsp;&nbsp;&nbsp;&nbsp;&nbsp; <span class="contact"><svg class="icon" viewBox="0 0 10 10"><rect x="0.7" y="2" width="8.6" height="6" fill="none" stroke="#111"/></svg>info@corwinlestak.com</span></div>
      <div class="contact" style="margin-top:-3px">Social media handles: @corwinlestak</div>
    </div>
  </footer>
</section>

<section class="sheet envelope-back" aria-label="Envelope back">
  <svg width="555" height="90" viewBox="0 0 555 90">
    <path d="M0 0 L12 72 Q14 83 28 83 L527 83 Q541 83 543 72 L555 0" fill="#fff" stroke="#c9c9c9" stroke-width="1.2"/>
    <path d="M13 78 Q16 85 28 85 L527 85 Q539 85 542 78" fill="none" stroke="#e2e2e2" stroke-width="2"/>
  </svg>
</section>

</body>
</html>
```